High-End Medical Center Website Design Project

This design is part of a well thought-out project by an experienced project manager / developer. The approved wireframe is attached. Creative interpretations / suggestions based on the layout encouraged.

The design is for a new state-of-the-art medical center located in Dallas, Texas. The target audience would likely be individuals (approx. 60% female /40% male) who are the healthcare decision-makers for their families. They would likely have insurance and be inclined to seek out top-quality care.

Potential clients would choose this client over others in their industry because the medical center is physician owned, meaning it is patient-focused rather than profit-focused. The facility is brand new, featuring the latest technology. (This includes an amazing waiting room featuring WiFi and docking stations.) The physicians are hand-picked by referral only.

The look of the site should be extremely clean. We are going for a well-organized, professional look with a bit of a warm glow (interpret that however you like). Use crisp corners and the colors in the logo.

Think modern, clean with some great use of color / font.

We can get lovely photography of the medical center once construction is complete. Feel free to use an "example image" behind the Featured Area ("Physician Owned. Patient-Focused") if you like. We are open to ideas.

ONE CHANGE REQUESTED IN THE WIREFRAME:

Remove the "Connect" 1/4 page footer area and replace with a quick contact form. You may swap the "Locations" area with the form if desired. Put social media icons at the top left of the page in the top header area.

(Note: Please use social media icons that match the design rather than standard icons. We preferred not placing the icons at the top, but the client requested this. Let's not bring more attention to them than necessary.)
Updates

We're custom programming this site, so there's no need to base it on a template. Also, we would prefer not to use typical "seen everywhere" stock images.Thanks.

Industry/Entity Type

Construction

Requirements
Must have
• Follow the wireframe. This has been approved.
Nice to have
• Examples of what hover states, links or dropdowns might look like.

```html
<!DOCTYPE html>
<html lang="en">
<head>
<meta charset="utf-8">
<title>Nova Medical Center</title>
<link href="https://fonts.googleapis.com/css2?family=Ubuntu:ital,wght@0,300;0,400;0,500;0,700;1,400&family=Arimo:wght@400;700&display=swap" rel="stylesheet">
<style>
:root{
  --teal:#44a8b8;
  --teal-text:#2e9db2;
  --teal-dark:#1f8296;
  --blue:#065aab;
  --blue-menu:#3a5fb0;
  --blue-menu-dark:#3253a3;
  --ink:#333;
  --muted:#666;
  --line:#cfd8dc;
  --white:#fff;
}
*{box-sizing:border-box;margin:0;padding:0}
html,body{width:1003px;height:1200px;overflow:hidden;background:var(--white)}
body{position:relative;font-family:"Arimo",Arial,sans-serif;color:var(--ink)}
.abs{position:absolute}
.ubuntu{font-family:"Ubuntu",sans-serif}

/* top bar */
.topbar{left:0;top:0;width:1003px;height:40px;border-bottom:1px solid var(--teal)}
.social{top:8px;width:24px;height:24px;border-radius:50%;background:var(--teal)}
.phone{left:168px;top:14px;font:400 13px "Ubuntu",sans-serif;color:var(--teal-text);display:flex;align-items:center;gap:10px}
.search-box{left:765px;top:12px;width:123px;height:19px;border:1px solid var(--teal)}
.search-icon{left:898px;top:11px}

/* header */
.brand{left:67px;top:55px;height:44px;display:flex;align-items:center;gap:10px;font:700 30px "Ubuntu",sans-serif;color:var(--blue);letter-spacing:1px}
.brand-mark{width:30px;height:30px;background:var(--teal)}
.nav{left:440px;top:79px;display:flex;height:35px}
.nav a{display:flex;align-items:center;padding:0 7px;margin-left:8px;font:400 11.5px "Ubuntu",sans-serif;color:var(--teal-text);text-decoration:none;padding-top:8px}
.nav a.active{background:var(--blue-menu);color:var(--white);margin-left:8px}
.caret{font-size:8px;margin-left:3px}

/* hero */
.hero-bg{left:0;top:114px;width:1003px;height:344px;background:linear-gradient(90deg,#b9cbd4,#dbe6ea 10%,#dbe6ea 90%,#b9cbd4)}
.hero-photo{left:67px;top:114px;width:865px;height:344px;background:linear-gradient(90deg,#c9d6de 0%,#e8eef2 35%,#dfe8ee 70%,#eef3f6 100%);box-shadow:0 0 14px rgba(0,0,0,.25)}
.hero-band{left:67px;top:343px;width:865px;height:115px;background:rgba(52,105,175,.85)}
.hero-title{left:67px;top:354px;width:926px;text-align:center;font:300 22px "Ubuntu",sans-serif;color:var(--white)}
.hero-stars{left:67px;top:386px;width:926px;text-align:center;font-size:10px;letter-spacing:2px;color:var(--white)}
.hero-icon{top:409px;width:39px;height:39px;border-radius:50%;background:var(--white);display:flex;align-items:center;justify-content:center}
.dot{top:438px;width:12px;height:12px;border-radius:50%;border:2px solid var(--white);background:#333}
.dot.on{background:var(--teal)}

/* dropdown */
.dropdown{left:532px;top:114px;width:165px;background:var(--blue-menu);box-shadow:0 2px 4px rgba(0,0,0,.2)}
.dropdown li{list-style:none;height:33px;border-bottom:1px solid #3456a2;display:flex;align-items:center;justify-content:space-between;padding:0 12px 0 18px;font-size:10px;color:var(--white)}
.dropdown li.hover{background:var(--blue-menu-dark)}

/* features */
.features{left:68px;top:503px;width:864px;height:140px;background:var(--teal);display:flex}
.feature{height:140px;border-left:1px solid var(--white);color:var(--white);text-align:center;position:relative}
.feature:first-child{border-left:none}
.apart{width:220px;font-family:"Ubuntu",sans-serif;font-weight:300;padding-top:24px}
.apart .big{font-size:48px;line-height:50px}
.apart .mid{font-size:32px;line-height:38px}
.feature h3{font:300 19px "Ubuntu",sans-serif;margin-top:42px}
.feature p{font-size:10px;line-height:12px;margin:6px 10px 0}
.feature-badge{position:absolute;left:50%;top:-23px;margin-left:-30px;width:60px;height:52px;border-radius:0 0 30px 30px;background:var(--white);display:flex;align-items:center;justify-content:center}

/* content */
.article-photo{left:68px;top:686px;width:202px;height:138px;border:2px solid #d5d5d5;background:linear-gradient(135deg,#d9c9a8,#efe6d6 50%,#c9b8a6)}
.section-title{font:400 26px "Ubuntu",sans-serif;color:var(--teal-text)}
.article-text{left:288px;top:723px;width:252px;font-size:10.5px;line-height:12.2px;color:#222}
.readmore{left:289px;top:808px;font:italic 12px "Ubuntu",sans-serif;color:var(--blue);text-decoration:underline}
.divider{left:553px;top:686px;width:1px;height:158px;background:#bbb}
.arrow-btn{top:688px;width:22px;height:22px;background:var(--teal);display:flex;align-items:center;justify-content:center}
.testi-photo{left:565px;top:719px;width:90px;height:100px;border:2px solid #d5d5d5;background:linear-gradient(135deg,#e4e8ea,#cdd6da)}
.quote{left:685px;top:728px;width:250px;font:italic 13px "Ubuntu",sans-serif;line-height:15.2px;color:#666}
.quote-name{left:685px;top:803px;font:italic 700 12px "Ubuntu",sans-serif;color:var(--blue)}

/* footer */
.footer{left:0;top:872px;width:1003px;height:328px;background:var(--blue)}
.fcol-title{top:890px;font:400 26px "Ubuntu",sans-serif;color:var(--white);padding:0 0 0 5px;border-bottom:3px solid var(--white);width:147px;height:35px}
.flist{top:938px;list-style:none;color:var(--white);font-size:10px;line-height:12px}
.flist li{position:relative;padding-left:13px;height:44px}
.flist li::before{content:"›";position:absolute;left:1px;top:-2px;font-size:13px}
.address{left:403px;top:939px;color:var(--white);font-size:10px;line-height:16.5px}
.map{left:399px;top:1026px;width:148px;height:111px;background:linear-gradient(135deg,#c9cdd1,#e3e5e7 50%,#bfc4c8)}
.field{left:566px;width:145px;height:23px;background:var(--white);border-radius:3px;box-shadow:inset 0 1px 3px rgba(0,0,0,.3);font-size:9px;color:#777;padding:6px 5px}
.submit{left:566px;top:1114px;width:145px;height:23px;background:#7ec8d4;border:2px solid #5aaebd;font:700 13px "Arimo",sans-serif;color:var(--blue);text-align:center;line-height:19px;letter-spacing:1px}
.wait{left:728px;top:868px}
.wait-title{left:728px;top:890px;width:204px;text-align:center;font:300 24px "Ubuntu",sans-serif;line-height:30px;color:var(--white)}
.digit{top:960px;width:31px;height:46px;background:var(--white);border-radius:3px;font:700 38px "Ubuntu",sans-serif;color:var(--blue);text-align:center;line-height:46px}
.minutes{left:832px;top:971px;font:700 20px "Ubuntu",sans-serif;color:var(--white)}
.wait-text{left:748px;top:1032px;width:166px;text-align:center;font-size:10px;line-height:12px;color:var(--white)}
.foot-line{left:0;top:1162px;width:1003px;height:1px;background:rgba(255,255,255,.7)}
.copyright{left:0;top:1171px;width:1003px;text-align:center;font-size:10px;color:var(--white)}
</style>
</head>
<body>

<!-- top bar -->
<div class="abs topbar"></div>
<span class="abs social" style="left:76px"></span>
<span class="abs social" style="left:101px"></span>
<span class="abs social" style="left:126px"></span>
<div class="abs phone">
  <svg width="11" height="11" viewBox="0 0 24 24"><path fill="#2e9db2" d="M6.6 10.8a15 15 0 0 0 6.6 6.6l2.2-2.2c.3-.3.7-.4 1-.2 1.1.4 2.3.6 3.6.6.6 0 1 .4 1 1V20c0 .6-.4 1-1 1A17 17 0 0 1 3 4c0-.6.4-1 1-1h3.5c.6 0 1 .4 1 1 0 1.3.2 2.5.6 3.6.1.3 0 .7-.2 1z"/></svg>
  <span>(555) 210 - 4830</span>
</div>
<div class="abs search-box"></div>
<svg class="abs search-icon" width="20" height="20" viewBox="0 0 20 20"><circle cx="8" cy="8" r="6" fill="none" stroke="#2e9db2" stroke-width="2"/><line x1="12.5" y1="12.5" x2="18" y2="18" stroke="#2e9db2" stroke-width="2.4"/></svg>

<!-- header -->
<div class="abs brand"><span class="brand-mark"></span><span>NOVA MEDICAL CENTER</span></div>
<nav class="abs nav">
  <a>WHY NOVA</a>
  <a class="active">PHYCISIANS<span class="caret">⌄</span></a>
  <a style="margin-left:0">SPECIALTIES<span class="caret">⌄</span></a>
  <a style="margin-left:12px">INFO</a>
  <a style="margin-left:20px">LOCATIONS</a>
  <a style="margin-left:20px">CONTACT</a>
</nav>

<!-- hero -->
<div class="abs hero-bg"></div>
<div class="abs hero-photo" role="img" aria-label="Smiling physician in a white coat with a stethoscope, standing in a bright hospital corridor"></div>
<div class="abs hero-band"></div>
<div class="abs hero-title" style="left:67px;width:926px">Physician Owned, Patient Focused</div>
<div class="abs hero-stars" style="left:67px;width:926px">★★★★★★★★★★</div>
<div class="abs hero-icon" style="left:409px">
  <svg width="20" height="24" viewBox="0 0 20 24"><path d="M5 2v7a5 5 0 0 0 10 0V2" fill="none" stroke="#3a68b3" stroke-width="2.4"/><path d="M10 14v4" stroke="#3a68b3" stroke-width="2.4"/><circle cx="10" cy="20" r="3" fill="none" stroke="#3a68b3" stroke-width="2.2"/></svg>
</div>
<div class="abs hero-icon" style="left:510px">
  <svg width="22" height="22" viewBox="0 0 22 22"><path d="M2 6l11-4 7 9-11 9z" fill="#2f63b0"/></svg>
</div>
<div class="abs hero-icon" style="left:611px;font:700 22px 'Ubuntu',sans-serif;color:#3a68b3">?</div>
<span class="abs dot" style="left:76px"></span>
<span class="abs dot on" style="left:95px"></span>
<span class="abs dot" style="left:114px"></span>
<span class="abs dot" style="left:133px"></span>

<!-- dropdown -->
<ul class="abs dropdown">
  <li>Sub Item 1</li>
  <li class="hover">Sub Item 1</li>
  <li>Sub Item 1</li>
  <li>Sub Item 1</li>
  <li>Sub Item 1</li>
  <li>Sub Item 2<span style="font-size:14px">›</span></li>
</ul>

<!-- features -->
<section class="abs features">
  <div class="feature apart"><div class="big">What</div><div class="mid">Set Us Apart</div></div>
  <div class="feature" style="width:210px">
    <span class="feature-badge"><svg width="30" height="36" viewBox="0 0 30 36"><rect x="9" y="4" width="12" height="28" rx="6" transform="rotate(30 15 18)" fill="none" stroke="#222" stroke-width="2.5"/><circle cx="12" cy="24" r="2" fill="#222"/><circle cx="16" cy="20" r="1.6" fill="#222"/></svg></span>
    <h3>Technology</h3>
    <p>Lorem ipsum dolor sit amet, consec-tetur adipiscing elit. Nullam ullamcor-per orci sit amet velit laoreet varius. Suspendisse sit amet mattis dolor, vel</p>
  </div>
  <div class="feature" style="width:222px">
    <span class="feature-badge"><svg width="32" height="28" viewBox="0 0 32 28"><rect x="2" y="7" width="28" height="19" rx="2" fill="none" stroke="#222" stroke-width="2.5"/><path d="M11 7V3h10v4" fill="none" stroke="#222" stroke-width="2.5"/><path d="M16 11v11M10.5 16.5h11" stroke="#222" stroke-width="3"/></svg></span>
    <h3>Quality of Care</h3>
    <p>Lorem ipsum dolor sit amet, consec-tetur adipiscing elit. Nullam ullamcor-per orci sit amet velit laoreet varius. Suspendisse sit amet mattis dolor, vel</p>
  </div>
  <div class="feature" style="width:212px">
    <span class="feature-badge"><svg width="30" height="36" viewBox="0 0 30 36"><line x1="15" y1="2" x2="15" y2="34" stroke="#222" stroke-width="2.5"/><path d="M3 7c6 3 18 3 24 0" fill="none" stroke="#222" stroke-width="2.5"/><path d="M10 14c6 3 4 7 0 9 4 2 4 5 1 7M20 14c-6 3-4 7 0 9-4 2-4 5-1 7" fill="none" stroke="#222" stroke-width="1.6"/></svg></span>
    <h3>Patient Experience</h3>
    <p>Lorem ipsum dolor sit amet, consec-tetur adipiscing elit. Nullam ullamcor-per orci sit amet velit laoreet varius. Suspendisse sit amet mattis dolor, vel</p>
  </div>
</section>

<!-- content -->
<div class="abs article-photo" role="img" aria-label="Doctor listening to a young patient's heartbeat with a stethoscope"></div>
<h2 class="abs section-title" style="left:287px;top:687px">Headings</h2>
<p class="abs article-text">Lorem ipsum dolor sit amet, consectetur adipiscing elit. Nullam ullamcorper orci sit amet velit laoreet varius. Suspendisse sit amet mattis dolor, vel condimentum justo. Ut eu eros iaculis, blandit massa at, commodo justo. Aliquam erat volutpat. Praesent mollis dolor nunc, non pellentesque nulla sagittis vitae. Suspendisse</p>
<a class="abs readmore">readmore</a>
<div class="abs divider"></div>
<h2 class="abs section-title" style="left:562px;top:687px">Testimonials</h2>
<span class="abs arrow-btn" style="left:884px"><svg width="8" height="10"><path d="M6 1L2 5l4 4" fill="none" stroke="#fff" stroke-width="1.5"/></svg></span>
<span class="abs arrow-btn" style="left:909px"><svg width="8" height="10"><path d="M2 1l4 4-4 4" fill="none" stroke="#fff" stroke-width="1.5"/></svg></span>
<div class="abs testi-photo" role="img" aria-label="Portrait of a smiling patient"></div>
<svg class="abs" style="left:662px;top:760px" width="12" height="24"><path d="M11 0L1 12l10 12" fill="#fff" stroke="#ccc"/></svg>
<p class="abs quote">Donec dictum sodales ligula vel varius. Aenean eget magna sed nunc posuere fringilla. In tincidunt, turpis at tempor porta, massa odio vestibulum ante, vitae</p>
<div class="abs quote-name">Marcus</div>

<!-- footer -->
<footer class="abs footer"></footer>
<h3 class="abs fcol-title" style="left:68px">News</h3>
<h3 class="abs fcol-title" style="left:234px">Blog</h3>
<h3 class="abs fcol-title" style="left:399px">Location</h3>
<h3 class="abs fcol-title" style="left:565px">Contact</h3>
<ul class="abs flist" style="left:73px;width:140px">
  <li>Lorem ipsum dolor sit amet, consectetur adipisc-</li>
  <li>Lorem ipsum dolor sit amet, consectetur adipisc-</li>
  <li>Lorem ipsum dolor sit amet, consectetur adipisc-</li>
  <li>Lorem ipsum dolor sit amet, consectetur adipisc-</li>
  <li>Lorem ipsum dolor sit amet, consectetur adipisc-</li>
</ul>
<ul class="abs flist" style="left:239px;width:145px">
  <li>Lorem ipsum dolor sit amet, consectetur adipiscing elit.</li>
  <li>Lorem ipsum dolor sit amet, consectetur adipiscing elit.</li>
  <li>Lorem ipsum dolor sit amet, consectetur adipiscing elit.</li>
  <li>Lorem ipsum dolor sit amet, consectetur adipiscing elit.</li>
  <li>Lorem ipsum dolor sit amet, consectetur adipiscing elit.</li>
</ul>
<address class="abs address" style="font-style:normal">
  Nova Medical Center<br>
  2250 Meridian Park Blvd Suite B<br>
  Dallas, Texas 75201<br>
  Phone: (214) 555-0142<br>
  Fax: (214) 555-0143
</address>
<div class="abs map" role="img" aria-label="Street map showing the medical center location"></div>
<div class="abs field" style="top:937px">Name</div>
<div class="abs field" style="top:972px">Telp</div>
<div class="abs field" style="top:1008px">Email</div>
<div class="abs field" style="top:1043px;height:60px"></div>
<div class="abs submit">SUBMIT</div>

<svg class="abs wait" width="204" height="274" viewBox="0 0 204 274"><defs><filter id="shade" x="-10%" y="-10%" width="120%" height="120%"><feDropShadow dx="0" dy="2" stdDeviation="3" flood-opacity=".35"/></filter></defs><path d="M0 0h204v228l-102 44L0 228z" fill="#47a9ba" filter="url(#shade)"/></svg>
<div class="abs wait-title">Averange<br>wait time</div>
<div class="abs digit" style="left:753px">0</div>
<div class="abs digit" style="left:787px">8</div>
<div class="abs minutes">minutes</div>
<p class="abs wait-text">Lorem ipsum dolor sit amet, consectetur adipiscing elit. Nullam ullamcorper orci sit amet velit laoreet varius. Suspendisse sit amet</p>

<div class="abs foot-line"></div>
<div class="abs copyright">Copyright © 2013. All rights reserved. Terms and Condition | Privacy | Sitemap</div>

</body>
</html>
```